Velvet Afterhours Poster Design

Need poster design made up in next few days, can guarantee payment to winner. Poster must contain the following but feel free to word it better:
Velvet Afterhours
Presented by quendor Sounds
Select resident djs
Drink specials all night
Open from 8pm to 12pm
Find us on Friendwall
At Marlow Suites every Saturday
These will be on posters and fliers
Of a3 and roughly a5 size.
Our target audience is people 18-25
We want the posters to be exciting and professional. We would like a blue or purple with black color scheme but there is plenty of room for creative license so have a play around with what you think looks good. We currently don't have a logo but if your including one we would like to see it as c6 as in carbon as an element. Our first drink special is cocktails in jars but is not essential to include, can provide proper copy of the picture if you want to include it in your design. Please contact us if you need more information. we will be quick to pick a winner so payment will be provided fast!!!
Thank you all in advance for your submissions!!

```html
<!DOCTYPE html>
<html lang="en">
<head>
<meta charset="utf-8">
<title>Velvet Afterhours – Saturday Poster</title>
<link rel="stylesheet" href="https://fonts.googleapis.com/css2?family=Bebas+Neue&family=Righteous&family=Josefin+Sans:wght@400&display=swap">
<style>
  :root {
    --page: #ffffff;
    --paper: #ffffff;
    --paper-tint: #e8eee4;
    --green: #9ccc6c;
    --green-mid: #86ae5c;
    --green-dark: #6b8a47;
    --green-pale: #cfe6b6;
    --ink: #0c0f0c;
    --white: #ffffff;
  }
  html, body {
    margin: 0;
    width: 1200px;
    height: 1000px;
    overflow: hidden;
    background: var(--page);
  }
  .poster {
    position: absolute;
    left: 273px;
    top: 37px;
    width: 652px;
    height: 925px;
    box-shadow: 0 1px 5px rgba(0,0,0,.25);
  }
  .canvas { position: absolute; left: 0; top: 0; }
  .title { font-family: "Righteous", sans-serif; fill: var(--ink); }
  .presenter { font-family: "Righteous", sans-serif; fill: var(--ink); font-size: 17px; }
  .schedule { font-family: "Josefin Sans", sans-serif; fill: var(--white); font-size: 19px; letter-spacing: 5px; }
  .banner-text { font-family: "Bebas Neue", sans-serif; fill: var(--white); }
  .brand-name { font-family: "Righteous", sans-serif; fill: var(--ink); font-size: 20px; }
  .footer-text { font-family: "Josefin Sans", sans-serif; fill: var(--green); font-size: 21px; letter-spacing: 6px; }
</style>
</head>
<body>
<div class="poster"></div>
<svg class="canvas" width="1200" height="1000" viewBox="0 0 1200 1000" xmlns="http://www.w3.org/2000/svg">
  <!-- paper halves -->
  <rect class="paper-left" x="273" y="37" width="326" height="925" fill="var(--paper)"/>
  <rect class="paper-right" x="599" y="37" width="326" height="925" fill="var(--paper-tint)"/>

  <!-- header ribbons -->
  <g class="ribbons">
    <polygon points="273,197 340,197 273,258" fill="var(--green-dark)"/>
    <polygon points="273,278 362,278 302,341 273,341" fill="var(--green-dark)"/>
    <rect x="273" y="135" width="130" height="62" fill="var(--green)"/>
    <rect x="273" y="215" width="89" height="63" fill="var(--green)"/>

    <polygon points="925,197 858,197 925,258" fill="var(--green-dark)"/>
    <polygon points="925,278 835,278 896,341 925,341" fill="var(--green-dark)"/>
    <rect x="795" y="135" width="130" height="62" fill="var(--green)"/>
    <rect x="835" y="215" width="90" height="63" fill="var(--green)"/>
  </g>

  <!-- jar drawings -->
  <rect x="281" y="80" width="38" height="52" fill="var(--green-pale)" role="img" aria-label="Cocktail jar illustration"/>
  <rect x="330" y="96" width="28" height="36" fill="var(--green-pale)" role="img" aria-label="Cocktail jar illustration"/>
  <rect x="795" y="96" width="38" height="36" fill="var(--green-pale)" role="img" aria-label="Cocktail jar illustration"/>
  <rect x="869" y="80" width="38" height="52" fill="var(--green-pale)" role="img" aria-label="Cocktail jar illustration"/>
  <rect x="838" y="848" width="46" height="60" fill="var(--green-pale)" role="img" aria-label="Cocktail jar illustration"/>

  <!-- title -->
  <text class="title" x="599" y="188" text-anchor="middle" font-size="64" textLength="300" lengthAdjust="spacingAndGlyphs">VELVET</text>
  <text class="title" x="599" y="272" text-anchor="middle" font-size="64" textLength="400" lengthAdjust="spacingAndGlyphs">AFTERHOURS</text>
  <text class="presenter" x="599" y="314" text-anchor="middle">presented by quendor sounds</text>

  <!-- schedule band -->
  <defs>
    <linearGradient id="bandGrad" x1="0" x2="1">
      <stop offset="0" stop-color="var(--green)"/>
      <stop offset="1" stop-color="var(--green-mid)"/>
    </linearGradient>
  </defs>
  <rect class="schedule-band" x="273" y="341" width="652" height="27" fill="url(#bandGrad)"/>
  <text class="schedule" x="599" y="362" text-anchor="middle">EVERY SATURDAY • 8 - 12PM</text>

  <!-- brand mark -->
  <circle cx="540" cy="455" r="22" fill="none" stroke="var(--ink)" stroke-width="7"/>
  <text class="brand-name" x="572" y="462">Velvet Afterhours</text>

  <!-- chevron banners -->
  <g class="chevrons">
    <polygon points="273,453 599,547 599,655 273,562" fill="var(--green)"/>
    <polygon points="599,547 925,453 925,562 599,655" fill="var(--green-mid)"/>
    <polygon points="273,600 599,692 599,775 273,683" fill="var(--green)"/>
    <polygon points="599,692 925,600 925,683 599,775" fill="var(--green-mid)"/>
    <polygon points="273,725 599,818 599,880 273,790" fill="var(--green)"/>
    <polygon points="599,818 925,725 925,790 599,880" fill="var(--green-mid)"/>
  </g>

  <g class="banner-text">
    <text transform="translate(318,561) skewY(16)" font-size="98" textLength="230" lengthAdjust="spacingAndGlyphs">SELECT</text>
    <text transform="translate(608,626) skewY(-16)" font-size="70" textLength="304" lengthAdjust="spacingAndGlyphs">RESIDENT DJS</text>
    <text transform="translate(285,664) skewY(16)" font-size="64" textLength="306" lengthAdjust="spacingAndGlyphs">DRINK SPECIALS</text>
    <text transform="translate(627,757) skewY(-16)" font-size="92" textLength="272" lengthAdjust="spacingAndGlyphs">ALL NIGHT</text>
    <text transform="translate(293,775) skewY(16)" font-size="56" textLength="276" lengthAdjust="spacingAndGlyphs">AT MARLOW SUITES</text>
    <text transform="translate(607,863) skewY(-16)" font-size="58" textLength="306" lengthAdjust="spacingAndGlyphs">EVERY SATURDAY</text>
  </g>

  <!-- footer -->
  <rect class="footer" x="273" y="913" width="652" height="49" fill="var(--ink)"/>
  <text class="footer-text" x="582" y="946" text-anchor="middle">FIND US ON FRIENDWALL</text>
  <rect x="794" y="926" width="22" height="22" rx="3" fill="var(--green-dark)"/>
</svg>
</body>
</html>
```